New Zealand Luggage Importer Needs Business Cards

We need professional, creative and fashionable business cards created.
We are based in New Zealand and import and distribute high-end, quality, fashionable and durable luggage.
We pride ourselves on selling the very best quality luggage, second only to 1 brand (which we won't mention here)...we use the same manufacturer. However, our prices are much more reasonable.
Business
Sam Ortiz
027 481 2956
3/17 Kestrel Lane, Morrow Flats, Auckland, 0614
PO Box 208354, North Shore, Auckland 0792
09-527-3061
sales@brindlecases.co.nz / www.brindlecases.co.nz

```html
<!DOCTYPE html>
<html lang="en">
<head>
<meta charset="utf-8">
<title>Brindle Cases — Business Card</title>
<link rel="stylesheet" href="https://fonts.googleapis.com/css2?family=Raleway:wght@300;400;600;700&family=Open+Sans:wght@300;400&display=swap">
<style>
  :root {
    --page-bg: #f1f1f1;
    --card-bg: #1c1c1c;
    --card-bg-deep: #141414;
    --gold: #cdaa5c;
    --white: #ffffff;
    --text-soft: #c9c9c9;
    --text-muted: #9a9a9a;
    --map-tone: #3a3a3a;
  }
  * { box-sizing: border-box; margin: 0; padding: 0; }
  html, body {
    width: 1200px;
    height: 1000px;
    overflow: hidden;
    background: var(--page-bg);
  }
  .sheet {
    position: relative;
    width: 1200px;
    height: 1000px;
  }
  .card {
    position: absolute;
    left: 180px;
    width: 840px;
    height: 450px;
    border-radius: 18px;
    background: radial-gradient(ellipse at 40% 40%, var(--card-bg) 0%, var(--card-bg-deep) 100%);
    box-shadow: 0 4px 14px rgba(0, 0, 0, 0.18);
    overflow: hidden;
  }
  .card--front { top: 40px; }
  .card--back { top: 510px; }

  /* Front */
  .country-map {
    position: absolute;
    left: 560px;
    top: 50px;
    width: 230px;
    height: 350px;
    border-radius: 40% 30% 45% 35%;
    background: linear-gradient(200deg, var(--map-tone) 0%, rgba(58, 58, 58, 0.55) 100%);
    opacity: 0.8;
  }
  .brand-name {
    position: absolute;
    left: 0;
    right: 0;
    top: 186px;
    text-align: center;
    font-family: 'Raleway', sans-serif;
    font-weight: 700;
    font-size: 50px;
    letter-spacing: 3px;
    color: var(--white);
  }
  .front-web {
    position: absolute;
    left: 0;
    right: 0;
    top: 376px;
    text-align: center;
    font-family: 'Open Sans', sans-serif;
    font-weight: 300;
    font-size: 18px;
    letter-spacing: 3px;
    color: var(--text-muted);
  }
  .front-web .accent { color: var(--gold); }

  /* Back */
  .person {
    position: absolute;
    left: 60px;
    top: 112px;
    font-family: 'Raleway', sans-serif;
  }
  .person-name {
    font-size: 36px;
    font-weight: 400;
    color: var(--gold);
    letter-spacing: 0.5px;
  }
  .person-name .first { font-weight: 700; color: var(--white); }
  .person-role {
    margin-top: 2px;
    font-size: 20px;
    font-weight: 400;
    color: var(--text-soft);
  }
  .contacts {
    position: absolute;
    left: 62px;
    top: 232px;
    list-style: none;
    font-family: 'Open Sans', sans-serif;
    font-size: 18px;
    color: var(--text-soft);
  }
  .contact {
    display: flex;
    align-items: center;
    height: 27px;
  }
  .contact--gap { margin-top: 16px; }
  .contact-icon {
    width: 16px;
    height: 16px;
    margin-right: 22px;
    fill: none;
    stroke: var(--gold);
    stroke-width: 2;
    stroke-linecap: round;
    stroke-linejoin: round;
  }
  .contact-icon--solid { fill: var(--gold); stroke: none; }
  .contact .accent { color: var(--gold); }
  .address {
    position: absolute;
    left: 62px;
    top: 392px;
    font-family: 'Open Sans', sans-serif;
    font-size: 19px;
    line-height: 27px;
    color: var(--text-muted);
  }
</style>
</head>
<body>
<main class="sheet">

  <section class="card card--front" aria-label="Business card front">
    <div class="country-map" role="img" aria-label="Faint silhouette map of New Zealand"></div>
    <h1 class="brand-name">BRINDLE CASES</h1>
    <p class="front-web">www.<span class="accent">brindlecases</span>.co.nz</p>
  </section>

  <section class="card card--back" aria-label="Business card back">
    <div class="person">
      <h2 class="person-name"><span class="first">SAM</span> ORTIZ</h2>
      <p class="person-role">Owner</p>
    </div>

    <ul class="contacts">
      <li class="contact">
        <svg class="contact-icon contact-icon--solid" viewBox="0 0 16 16" aria-hidden="true">
          <path d="M3.2 1.5l2.4 0 1.1 3-1.6 1.2c.8 1.8 2.2 3.2 4 4l1.2-1.6 3 1.1 0 2.4c0 .8-.7 1.4-1.5 1.4C6.6 13 3 9.4 1.8 3 1.8 2.2 2.4 1.5 3.2 1.5z"/>
        </svg>
        <span>027 481 2956</span>
      </li>
      <li class="contact">
        <svg class="contact-icon contact-icon--solid" viewBox="0 0 16 16" aria-hidden="true">
          <path d="M1 5.5C3 3 13 3 15 5.5l-.6 1.8-3-.6V5.8H4.6v.9l-3 .6z"/>
          <path d="M4.5 8h7l2 6h-11z"/>
        </svg>
        <span>09-527-3061</span>
      </li>
      <li class="contact contact--gap">
        <svg class="contact-icon" viewBox="0 0 16 16" aria-hidden="true">
          <path d="M14.5 1.5L1.5 7l5.5 2 2 5.5z"/>
          <path d="M14.5 1.5L7 9"/>
        </svg>
        <span>sales@brindlecases.co.nz</span>
      </li>
      <li class="contact">
        <svg class="contact-icon" viewBox="0 0 16 16" aria-hidden="true">
          <circle cx="9.5" cy="6.5" r="4.5"/>
          <path d="M6.3 9.7L1.8 14.2"/>
        </svg>
        <span>www.<span class="accent">brindlecases</span>.co.nz</span>
      </li>
    </ul>

    <address class="address">
      3/17 Kestrel Lane, Morrow Flats, Auckland, 0614<br>
      PO Box 208354, North Shore, Auckland 0792
    </address>
  </section>

</main>
</body>
</html>
```